Real Estate Investment Company Needs A Business Card Designed

I need a business card designed for my use. We are a real estate investment company based in Omaha, Nebraska that specializes in buying, rehabbing and selling single family and multifamily properties. Would love designs that incorporate our logo and colors

Industry/Entity Type

Business

Contact Information for Business Card

Mitchell Parkhurst | President & CEO
4873 North 52nd Avenue, Ste 700
Omaha, NE 68142
(402) 786-4259
mitchell@kestrelgateproperties.example
www.KestrelgateProperties.example

Font styles to use
Serif

Colors
0255a3
3276b5

Requirements
Must have
• Our logo

```html
<!DOCTYPE html>
<html lang="en">
<head>
<meta charset="utf-8">
<title>Kestrelgate Properties – Business Card</title>
<link rel="stylesheet" href="https://fonts.googleapis.com/css2?family=Roboto+Condensed:wght@400;700&display=swap">
<style>
  :root {
    --backdrop: #b4b4b4;
    --card: #f1f1f1;
    --brand-blue: #0255a3;
    --brand-blue-light: #3276b5;
    --text-dark: #2b2b2b;
    --silver: #a9a9a9;
    --silver-light: #d2d2d2;
  }
  * { margin: 0; padding: 0; box-sizing: border-box; }
  html, body { width: 1200px; height: 576px; overflow: hidden; }
  body {
    background: var(--backdrop);
    font-family: "Roboto Condensed", Arial, sans-serif;
    position: relative;
  }
  .card {
    position: absolute;
    top: 138px;
    width: 484px;
    height: 294px;
    background: var(--card);
    border-radius: 12px;
    overflow: hidden;
    box-shadow: 0 3px 6px rgba(0,0,0,0.25);
  }
  .card--front { left: 82px; }
  .card--back { left: 602px; }

  .brand-mark {
    position: absolute;
    border-radius: 50%;
    background: var(--brand-blue);
  }
  .card--front .brand-mark { left: 36px; top: 69px; width: 194px; height: 194px; }
  .card--back .brand-mark { left: 63px; top: 50px; width: 120px; height: 120px; }

  .brand-name {
    position: absolute;
    color: var(--brand-blue);
    font-weight: 700;
    text-transform: uppercase;
    line-height: 1;
    text-align: center;
  }
  .brand-name span { display: block; }
  .brand-name .brand-sub { letter-spacing: 0.28em; margin-top: 4px; }
  .card--front .brand-name { left: 250px; top: 165px; font-size: 30px; }
  .card--front .brand-name .brand-sub { font-size: 14px; }
  .card--back .brand-name { left: 44px; top: 184px; width: 160px; font-size: 22px; }
  .card--back .brand-name .brand-sub { font-size: 10px; }

  .contact {
    position: absolute;
    left: 247px;
    top: 63px;
    color: var(--text-dark);
  }
  .contact-name {
    font-size: 20px;
    font-weight: 700;
    color: var(--brand-blue);
    line-height: 1.1;
  }
  .contact-name .surname { color: var(--brand-blue-light); }
  .contact-title { font-size: 12.5px; margin-top: 2px; }
  .contact-address { font-size: 13px; line-height: 18px; margin-top: 16px; }
  .contact-lines { list-style: none; margin-top: 8px; font-size: 12px; line-height: 19px; }
  .contact-lines li { display: flex; align-items: center; gap: 9px; white-space: nowrap; }
  .contact-lines svg { width: 11px; height: 11px; flex: none; fill: var(--brand-blue); }

  .footer-band {
    position: absolute;
    left: 0; bottom: 0;
    width: 484px; height: 40px;
  }
  .website {
    position: absolute;
    left: 247px;
    bottom: 12px;
    font-size: 12.5px;
    color: #ffffff;
  }
</style>
</head>
<body>

  <section class="card card--front">
    <div class="brand-mark"></div>
    <div class="brand-name">
      <span>Kestrelgate</span>
      <span class="brand-sub">Properties</span>
    </div>
  </section>

  <section class="card card--back">
    <div class="brand-mark"></div>
    <div class="brand-name">
      <span>Kestrelgate</span>
      <span class="brand-sub">Properties</span>
    </div>

    <div class="contact">
      <p class="contact-name">Mitchell <span class="surname">Parkhurst</span></p>
      <p class="contact-title">President &amp; CEO</p>
      <p class="contact-address">4873 North 52nd Avenue, Ste 700<br>Omaha, NE 68142</p>
      <ul class="contact-lines">
        <li>
          <svg viewBox="0 0 24 24" aria-hidden="true"><path d="M6.6 10.8a15.1 15.1 0 0 0 6.6 6.6l2.2-2.2a1 1 0 0 1 1-.25 11.4 11.4 0 0 0 3.6.57 1 1 0 0 1 1 1V20a1 1 0 0 1-1 1A17 17 0 0 1 3 4a1 1 0 0 1 1-1h3.5a1 1 0 0 1 1 1c0 1.25.2 2.45.57 3.57a1 1 0 0 1-.25 1z"/></svg>
          (402) 786-4259
        </li>
        <li>
          <svg viewBox="0 0 24 24" aria-hidden="true"><path d="M2 5h20v14H2z M4 7l8 6 8-6" fill="none" stroke="#0255a3" stroke-width="2.4"/></svg>
          mitchell@kestrelgateproperties.example
        </li>
      </ul>
    </div>

    <svg class="footer-band" viewBox="0 0 484 40" aria-hidden="true">
      <defs>
        <linearGradient id="band-silver" x1="0" y1="0" x2="1" y2="0">
          <stop offset="0" stop-color="#bdbdbd"/>
          <stop offset="1" stop-color="#e4e4e4"/>
        </linearGradient>
        <linearGradient id="band-blue" x1="0" y1="0" x2="1" y2="0">
          <stop offset="0" stop-color="#0255a3"/>
          <stop offset="1" stop-color="#3276b5"/>
        </linearGradient>
      </defs>
      <rect x="0" y="18" width="484" height="22" fill="url(#band-silver)"/>
      <polygon points="218,0 484,0 484,40 198,40" fill="url(#band-blue)"/>
    </svg>
    <p class="website">www.KestrelgateProperties.example</p>
  </section>

</body>
</html>
```